Brightmoor Partners Branding Revamp

We are a consulting company, looking for a way to display and promote our brand. We have 2 sides to the business- Brightmoor (financial) and Partners (cyber security). The financial side products relate to business necessities: card processing, website design/hosting/maintenance, VoIP phone systems. The cyber security side promotes a bundled package of 4 solutions: network vulnerability scan, dark web scan, anti-ransomeware/malware software, and image-level backups. We want people to understand that partnering with Brightmoor Partners gives them “Elevated Peace of Mind” (tagline). Current badge and logos uploaded.

Target Market(s)

Small businesses

Contact Information for Business Card

Lena Marwick, Vice President, lena@brightmoorpartners.example, 555-806-1937, www.brightmoorpartners.example

Requirements
Nice to have
• I do prefer the darker background for front and back

```html
<!DOCTYPE html>
<html lang="en">
<head>
<meta charset="utf-8">
<title>Brightmoor Partners – Business Card</title>
<link href="https://fonts.googleapis.com/css2?family=Cinzel:wght@400&family=Open+Sans:wght@400;600;700&display=swap" rel="stylesheet">
<style>
  :root {
    --canvas: #e4e4e4;
    --card: #262626;
    --card-deep: #1b1b1b;
    --red: #d0202e;
    --red-dark: #8e1119;
    --red-light: #e2343f;
    --white: #f2f2f2;
    --grey: #cfcfcf;
  }
  * { margin: 0; padding: 0; box-sizing: border-box; }
  html, body { width: 992px; height: 1200px; overflow: hidden; }
  body { background: var(--canvas); font-family: "Open Sans", sans-serif; position: relative; }

  .card {
    position: absolute; left: 76px; width: 840px; height: 480px;
    background: radial-gradient(ellipse at 60% 40%, #333 0%, var(--card) 45%, var(--card-deep) 100%);
    overflow: hidden;
    box-shadow: 0 10px 30px rgba(0,0,0,.35);
  }
  .card-front { top: 70px; }
  .card-back { top: 650px; }

  .stripe { position: absolute; left: 0; top: 0; }

  .wordmark {
    position: absolute; color: var(--white); font-weight: 600;
    letter-spacing: .28em; text-transform: uppercase;
    display: flex; flex-direction: column; align-items: flex-start; gap: 14px;
    line-height: 1.35;
  }
  .wordmark .mark-square { width: 22px; height: 22px; background: var(--red); flex: none; }
  .front-wordmark { left: 56px; top: 150px; font-size: 20px; width: 240px; }
  .back-wordmark { left: 56px; top: 150px; font-size: 18px; gap: 16px; }
  .back-wordmark .mark-square { width: 120px; height: 120px; background: none; border: 6px solid var(--red); }

  .person { position: absolute; left: 430px; top: 44px; }
  .person-name { color: var(--red-light); font-weight: 700; font-size: 34px; line-height: 1.1; }
  .person-title { color: var(--white); font-size: 17px; margin-left: 28px; }

  .contact { position: absolute; color: var(--white); font-size: 17px; line-height: 24px; white-space: nowrap; }
  .contact-phone { left: 440px; top: 158px; }
  .contact-email { left: 477px; top: 213px; }
  .contact-web { left: 514px; top: 268px; }

  .service-band {
    position: absolute; left: 0; top: 330px; width: 840px; height: 76px;
    background: linear-gradient(90deg, var(--red) 0%, #b81824 60%, var(--red-dark) 100%);
    padding: 10px 0 0 52px; color: var(--white); font-size: 15px; line-height: 1.6;
  }
  .service-band strong { font-weight: 700; letter-spacing: .02em; }
  .band-mark {
    position: absolute; right: 34px; top: 28px; font-size: 12px; font-weight: 600;
    letter-spacing: .25em; text-transform: uppercase; color: var(--white);
  }

  .network-bg {
    position: absolute; inset: 0;
    background: radial-gradient(ellipse at 55% 40%, rgba(140,20,28,.22) 0%, rgba(0,0,0,0) 60%);
  }
  .tagline {
    position: absolute; left: 290px; top: 120px; font-family: "Cinzel", serif;
    font-size: 36px; color: var(--white); letter-spacing: .04em; white-space: nowrap;
  }
  .connect { position: absolute; left: 360px; top: 190px; display: flex; align-items: center; gap: 12px; color: var(--white); font-size: 17px; font-weight: 600; }
  .social-dot { width: 26px; height: 26px; border-radius: 50%; background: var(--red); }
</style>
</head>
<body>

<section class="card card-front">
  <svg class="stripe" width="840" height="480" viewBox="0 0 840 480" aria-hidden="true">
    <polygon points="190,0 240,0 470,330 420,330" fill="#a3161f"/>
    <polygon points="240,0 320,0 550,330 470,330" fill="var(--red)"/>
    <g fill="#2a2a2a" stroke="none">
      <circle cx="388" cy="170" r="24"/>
      <circle cx="425" cy="225" r="24"/>
      <circle cx="462" cy="280" r="24"/>
    </g>
    <g fill="none" stroke="var(--red-light)" stroke-width="2" stroke-linecap="round" stroke-linejoin="round">
      <path d="M379 161 q-3 9 5 17 q8 8 17 5 l-1 -5 l-5 -2 l-3 3 q-6 -3 -9 -9 l3 -3 l-2 -5 z"/>
      <rect x="413" y="217" width="24" height="16" rx="1"/>
      <path d="M413 218 l12 9 l12 -9"/>
      <circle cx="462" cy="280" r="11"/>
      <path d="M451 280 h22 M462 269 q-7 11 0 22 M462 269 q7 11 0 22"/>
    </g>
  </svg>

  <div class="wordmark front-wordmark"><span class="mark-square"></span><span>Brightmoor<br>Partners</span></div>

  <div class="person">
    <div class="person-name">Lena Marwick</div>
    <div class="person-title">Vice President</div>
  </div>

  <div class="contact contact-phone">555-806-1937</div>
  <div class="contact contact-email">lena@brightmoorpartners.example</div>
  <div class="contact contact-web">www.brightmoorpartners.example</div>

  <div class="service-band">
    <div><strong>FINANCIAL SECURITY</strong> | Card Processing • Website Design,</div>
    <div>Website Hosting / Maintenance • VoIP Phone Systems</div>
    <span class="band-mark">Brightmoor Partners</span>
  </div>
</section>

<section class="card card-back">
  <div class="network-bg" role="img" aria-label="Faint red line network pattern across the dark background"></div>

  <div class="wordmark back-wordmark"><span class="mark-square"></span><span>Brightmoor Partners</span></div>

  <div class="tagline">Elevated Peace of Mind</div>
  <div class="connect">Connect With Us
    <span class="social-dot"></span><span class="social-dot"></span><span class="social-dot"></span>
  </div>

  <div class="service-band">
    <div><strong>CYBER SECURITY</strong> | Network Vulnerability Scan • Dark Web Scan,</div>
    <div>Anti-Ransomeware / Malware Software • Image-Level Backups</div>
    <span class="band-mark">Brightmoor Partners</span>
  </div>
</section>

</body>
</html>
```